A4 Single Page Brochure for Private Cloud Offerings

Theme: Futuristic Tech Company

Brightholm Systems is looking to offer private cloud services for our enterprise customers in Perth-based data-centres that provides our clients with a lower-cost alternative to Nimbra or QKS yielding better performance.

We are looking for a single A4 brochure with a great graphics design theme to promote these services.

We will be providing five tiers:
- Starter
- Growth
- Professional
- Premier
- Elite

Each plan must list on the brochure the Max VMs, CPU cores, Memory and SSD storage allocated. Refer to the uploaded PNG file.

The brochure must list the following selling points:

- Hosted in a local Perth-based TIER3 and TIER4 datacentres
- WA owned hosting - support local
- Low latency - ultra fast local hosting
- Includes Orvane Host Datacentre licensing
- Includes Valdrex Managed Firewalls for Enterprise level threat detection
- Includes all infrastructure maintenance services
- Full self management of VMs through customer portal
- Includes a 1gbps Internet link
- Predictable fixed monthly fee with no dynamic billing
- No additional charges for Storage Transactions, Internet Usage, VM Snapshots, Datacentre Bandwidth Usage and Firewall Traffic Usage.
- Highly available cluster, no single point of failure.
- Pricing is based on 36 months commit
- Yearly rate increases capped to a maximum of Australian CPI
- All plans have 24/7/365 support with dedicated after hours number.
- Managed backup and managed disaster recovery services can be added to plans

Service provided in accordance with our terms and conditions.

We need the ability to EDIT the brochure to adjust pricing after we receive the final project.

I have uploaded more details on these plans under the attachment PrivateCloudPlans.png.

Please do not utilise "Pushing the Boundaries of Technology" - our brand is being replaced with "Specialised Consulting". New website is under development but not launched yet.

Target Market(s)

Information Technology Sector

Colors
0054AA
0677BA
7BADD7
CADEEF
E8F1F8

Requirements
Must have
• Theme of Brightholm is Blue
Should not have
• Extremely stock imagary that just looks "cheap and stock"

```html
<!DOCTYPE html>
<html lang="en">
<head>
<meta charset="utf-8">
<title>Brightholm Private Cloud Plans</title>
<link href="https://fonts.googleapis.com/css2?family=Audiowide&family=Lato:wght@400;700;900&display=swap" rel="stylesheet">
<style>
  :root {
    --navy: #0b1c9c;
    --deep: #08206e;
    --royal: #0054aa;
    --ocean: #0677ba;
    --sky: #7badd7;
    --mist: #cadeef;
    --ice: #e8f1f8;
    --ink: #1d1d2b;
    --stage: #808080;
    --white: #ffffff;
  }
  * { margin: 0; padding: 0; box-sizing: border-box; }
  html, body { width: 1200px; height: 1000px; overflow: hidden; }
  body { background: var(--stage); font-family: "Lato", sans-serif; position: relative; }

  .brochure {
    position: absolute; left: 302px; top: 79px; width: 595px; height: 842px;
    background: var(--white); overflow: hidden;
  }

  /* Header */
  .brand {
    position: absolute; left: 36px; top: 34px;
    font-weight: 900; font-size: 17px; color: var(--navy); letter-spacing: 0.5px;
    font-family: "Lato", sans-serif;
  }
  .tagline-bands { position: absolute; left: 0; top: 0; width: 595px; height: 90px; }
  .tagline {
    position: absolute; left: 360px; top: 56px; width: 210px; text-align: center;
    font-family: "Audiowide", sans-serif; font-size: 10.5px; color: var(--white); letter-spacing: 1px;
  }

  .band {
    position: absolute; left: 0; width: 595px;
    background: linear-gradient(90deg, #0a2585 0%, #1450c4 45%, #1e62d8 60%, #0a2585 100%);
  }
  .band--top { top: 90px; height: 33px; }
  .band--mid { top: 398px; height: 32px; }

  .plans-title {
    position: absolute; top: 134px; left: 0; width: 595px; text-align: center;
    font-weight: 900; font-size: 14px; color: var(--navy); letter-spacing: 0.4px; word-spacing: 3px;
  }

  /* Plans table */
  .plans-head {
    position: absolute; top: 161px; left: 0; width: 595px; height: 36px;
    background: linear-gradient(90deg, var(--sky) 0%, #5b8fd6 35%, #1a3ab8 70%, var(--navy) 100%);
  }
  .row { position: absolute; left: 0; width: 595px; height: 34px; border-bottom: 1px solid #f0f4fa; }
  .row span { position: absolute; top: 50%; transform: translate(-50%, -50%); font-size: 11.5px; color: var(--ink); }
  .row .label { left: 62px; transform: translate(0, -50%); font-weight: 900; color: var(--navy); }
  .plans-head span { color: var(--white); font-weight: 700; font-size: 11.5px; }
  .c1 { left: 207px; } .c2 { left: 281px; } .c3 { left: 359px; } .c4 { left: 433px; } .c5 { left: 507px; }
  .r1 { top: 199px; } .r2 { top: 232px; } .r3 { top: 267px; } .r4 { top: 301px; }
  .cost {
    position: absolute; top: 334px; left: 0; width: 595px; height: 40px;
    background: linear-gradient(90deg, var(--ice) 0%, #cfe7f7 50%, #86cbf1 100%);
  }
  .cost span { font-weight: 900; font-size: 11.5px; color: var(--ink); }
  .cost .label { color: var(--ink); }
  .plans-note {
    position: absolute; top: 381px; left: 0; width: 595px; text-align: center;
    font-size: 7.5px; font-weight: 700; color: var(--navy);
  }

  /* Lower feature area */
  .features { position: absolute; left: 0; top: 430px; width: 595px; height: 412px; }
  .features svg { position: absolute; left: 0; top: 0; }
  .points { position: absolute; list-style: none; }
  .points li { position: absolute; padding-left: 12px; font-size: 10px; line-height: 12px; }
  .points li::before {
    content: ""; position: absolute; left: 0; top: 2px; width: 7px; height: 8px;
    clip-path: polygon(0 0, 45% 0, 100% 50%, 45% 100%, 0 100%, 55% 50%);
  }
  .points--dark { left: 324px; top: 17px; width: 262px; color: var(--white); }
  .points--dark li::before { background: var(--white); }
  .points--light { left: 19px; top: 216px; width: 260px; color: var(--ink); }
  .points--light li { font-weight: 700; }
  .points--light li::before { background: var(--navy); }
  .points--dark li { font-weight: 700; }
  .footer-note {
    position: absolute; right: 16px; bottom: 6px;
    font-size: 6.5px; color: var(--white); letter-spacing: 0.2px;
  }
</style>
</head>
<body>
<main class="brochure">

  <header>
    <div class="brand">Brightholm Systems</div>
    <svg class="tagline-bands" viewBox="0 0 595 90" aria-hidden="true">
      <defs>
        <linearGradient id="bandGrad" x1="0" x2="1" y1="0" y2="0">
          <stop offset="0" stop-color="#0a1f9c"/>
          <stop offset="0.55" stop-color="#2a7cf0"/>
          <stop offset="1" stop-color="#0b2ab0"/>
        </linearGradient>
      </defs>
      <polygon points="376,9 595,9 595,36 353,36" fill="url(#bandGrad)"/>
      <polygon points="352,41 595,41 595,82 308,82" fill="url(#bandGrad)"/>
    </svg>
    <div class="tagline">SPECIALISED CONSULTING</div>
  </header>

  <div class="band band--top"></div>
  <h1 class="plans-title">BRIGHTHOLM PRIVATE CLOUD PLANS</h1>

  <section class="plans">
    <div class="plans-head row">
      <span class="c1">Starter</span><span class="c2">Growth</span><span class="c3">Professional</span><span class="c4">Premier</span><span class="c5">Elite</span>
    </div>
    <div class="row r1"><span class="label">Max VMs</span><span class="c1">5</span><span class="c2">10</span><span class="c3">15</span><span class="c4">20</span><span class="c5">25</span></div>
    <div class="row r2"><span class="label">CPU cores</span><span class="c1">8</span><span class="c2">16</span><span class="c3">32</span><span class="c4">48</span><span class="c5">64</span></div>
    <div class="row r3"><span class="label">Memory (GB)</span><span class="c1">64</span><span class="c2">128</span><span class="c3">192</span><span class="c4">256</span><span class="c5">320</span></div>
    <div class="row r4"><span class="label">Storage SSD (TB)</span><span class="c1">3</span><span class="c2">8</span><span class="c3">15</span><span class="c4">20</span><span class="c5">30</span></div>
    <div class="row cost"><span class="label">Monthly Cost</span><span class="c1">$1028.01</span><span class="c2">$3426.64</span><span class="c3">$4626.05</span><span class="c4">$5482.72</span><span class="c5">$7196.07</span></div>
    <p class="plans-note">For larger plan, ask us.</p>
  </section>

  <div class="band band--mid"></div>

  <section class="features">
    <svg width="595" height="412" viewBox="0 0 595 412">
      <defs>
        <linearGradient id="photoTone" x1="0" y1="0" x2="1" y2="1">
          <stop offset="0" stop-color="#1d3f8f"/>
          <stop offset="0.45" stop-color="#121c4a"/>
          <stop offset="0.75" stop-color="#3a4a9a"/>
          <stop offset="1" stop-color="#1a2f8a"/>
        </linearGradient>
        <linearGradient id="panelTone" x1="0" y1="0" x2="1" y2="0">
          <stop offset="0" stop-color="#0b3f9c"/>
          <stop offset="1" stop-color="#0a3590"/>
        </linearGradient>
        <linearGradient id="whiteTone" x1="0" y1="0" x2="1" y2="0">
          <stop offset="0" stop-color="#ffffff" stop-opacity="0.97"/>
          <stop offset="1" stop-color="#eef2fa" stop-opacity="0.94"/>
        </linearGradient>
      </defs>
      <rect width="595" height="412" fill="url(#photoTone)" role="img" aria-label="Photo of a professional touching glowing security and data icons on a digital interface"/>
      <polygon points="309,0 595,0 595,219 309,219 257,108" fill="url(#panelTone)" opacity="0.95"/>
      <polygon points="0,197 275,197 321,303 275,412 0,412" fill="url(#whiteTone)"/>
      <polygon points="292,390 595,390 595,412 282,412" fill="#0a1c9a"/>
    </svg>

    <ul class="points points--dark">
      <li style="top:6px">Hosted in a local Perth-based TIER3 and TIER4 datacentres</li>
      <li style="top:37px">WA owned hosting - support local</li>
      <li style="top:58px">Low latency - ultra fast local hosting</li>
      <li style="top:80px">Includes Orvane Host Datacentre licensing</li>
      <li style="top:101px">Includes Valdrex Managed Firewalls for Enterprise level threat detection</li>
      <li style="top:132px">Includes all infrastructure maintenance services</li>
      <li style="top:152px">Full self management of VMs through customer portal</li>
      <li style="top:173px">Includes a 1gbps Internet link</li>
    </ul>

    <ul class="points points--light">
      <li style="top:0">Predictable fixed monthly fee with no dynamic billing</li>
      <li style="top:24px">No additional charges for Storage Transactions, Internet Usage, VM Snapshots, Datacentre Bandwidth Usage and Firewall Traffic Usage.</li>
      <li style="top:73px">Highly available cluster, no single point of failure.</li>
      <li style="top:97px">Pricing is based on 36 months commit</li>
      <li style="top:121px">All plans have 24/7/365 support with dedicated after hours number.</li>
      <li style="top:156px">Managed backup and managed disaster recovery services can be added to plans</li>
    </ul>

    <p class="footer-note">Service provided in accordance with our terms and conditions.</p>
  </section>

</main>
</body>
</html>
```